Mortgage Company needs some fresh looking business cards to replace current outdated design

Looking for fresh ideas. The only requirement is that the card must show the following:Keystead Logo (uploaded)Keystead slogan "your steady path home"Fair Dwelling Creditor logo (uploaded)Keystead NMLS #583017 (see current bus card, uploaded)Website as shown on sampleColor Codes as follows:Green = PMS 555 , #2b7051 , CMYK 83 33 77 21Rust = PMS 471 , #bc6225 , CMYK 21 70 100 8Would like two sided card. Front will have all of the above info, and back will have just the logo.

Target Market(s)

Consumers and Real Estate Agents

Industry/Entity Type

Mortgage Lender

Contact Information for Business Card

Color Codes as follows:
Green = PMS 555 , #2b7051 , CMYK 83 33 77 21
Rust = PMS 471 , #bc6225 , CMYK 21 70 100 8

Would like two sided card. Front will have all of the above info, and back will have just the logo.

Requirements
Must have
• Keystead Logo (uploaded)
• Keystead slogan "your steady path home"
• Fair Dwelling Creditor logo (uploaded)
• Keystead NMLS #583017 (see current bus card, uploaded)
• Website as shown on sample

```html
<!DOCTYPE html>
<html lang="en">
<head>
<meta charset="utf-8">
<title>Keystead Mortgage – Business Cards</title>
<link rel="stylesheet" href="https://fonts.googleapis.com/css2?family=Didact+Gothic&family=Playfair+Display:ital@0;1&display=swap">
<style>
  :root{
    --green:#2b7051;
    --rust:#bc6225;
    --charcoal:#2a2a2a;
    --ink:#222222;
    --grey:#555555;
    --paper:#ffffff;
    --backdrop:#e8e6e3;
  }
  *{margin:0;padding:0;box-sizing:border-box}
  html,body{width:1200px;height:1200px;overflow:hidden;background:var(--backdrop)}
  body{position:relative;font-family:"Didact Gothic",sans-serif;color:var(--ink)}
  .card{position:absolute;left:160px;width:880px;height:503px;background:var(--paper);overflow:hidden;box-shadow:0 6px 18px rgba(0,0,0,.18)}
  .card--back{top:48px}
  .card--front{top:620px}
  .card__corners{position:absolute;inset:0;width:100%;height:100%}
  .brand{position:absolute;display:flex;flex-direction:column}
  .brand__name{display:flex;align-items:center;gap:14px;color:var(--green);font-family:"Playfair Display",serif;line-height:1.05}
  .brand__mark{background:var(--green);flex:none}
  .brand__slogan{font-family:"Playfair Display",serif;font-style:italic;color:var(--rust);margin-top:10px}
  .card--back .brand{left:0;right:0;top:190px;align-items:center}
  .card--back .brand__name{font-size:58px}
  .card--back .brand__mark{width:30px;height:30px}
  .card--back .brand__slogan{font-size:30px}
  .card--front .brand{left:380px;top:110px;align-items:flex-start}
  .card--front .brand__name{font-size:40px}
  .card--front .brand__mark{width:22px;height:22px}
  .card--front .brand__slogan{font-size:21px;margin-left:120px}
  .person{position:absolute;left:48px;top:180px}
  .person__name{color:var(--rust);font-size:28px;letter-spacing:.5px;text-transform:uppercase}
  .person__role,.person__license{color:var(--grey);font-size:16px;margin-top:6px}
  .apply{position:absolute;left:48px;top:330px}
  .apply__label{font-size:15px;color:var(--grey)}
  .apply__url{font-size:22px;color:var(--ink);margin-top:4px}
  .contact{position:absolute;left:400px;top:270px;list-style:none;font-size:19px;line-height:1.5}
  .contact__item{display:flex;align-items:center;gap:10px}
  .contact__icon{width:18px;height:18px;flex:none}
  .contact__address{margin-top:2px}
  .lender-badge{position:absolute;right:30px;bottom:18px;width:40px;height:40px;border:4px solid var(--paper);border-radius:4px}
</style>
</head>
<body>

<section class="card card--back" aria-label="Card back">
  <svg class="card__corners" viewBox="0 0 880 503" aria-hidden="true">
    <path d="M0 0H360C240 18 120 60 0 150Z" fill="var(--charcoal)"/>
    <path d="M0 178C130 80 250 32 360 0L372 0C260 44 140 104 0 198Z" fill="var(--green)"/>
  </svg>
  <div class="brand">
    <div class="brand__name"><span class="brand__mark"></span>Keystead Mortgage</div>
    <div class="brand__slogan">your steady path home</div>
  </div>
</section>

<section class="card card--front" aria-label="Card front">
  <svg class="card__corners" viewBox="0 0 880 503" aria-hidden="true">
    <g>
      <path d="M0 0H300C200 16 100 50 0 120Z" fill="var(--charcoal)"/>
      <path d="M0 140C100 60 200 22 310 0L322 0C210 38 110 88 0 160Z" fill="var(--green)"/>
    </g>
    <g transform="rotate(180 440 251.5)">
      <path d="M0 0H300C200 16 100 50 0 120Z" fill="var(--charcoal)"/>
      <path d="M0 140C100 60 200 22 310 0L322 0C210 38 110 88 0 160Z" fill="var(--green)"/>
    </g>
  </svg>

  <div class="person">
    <div class="person__name">Dana Whitfield</div>
    <div class="person__role">Production Development Manager</div>
    <div class="person__license">NMLS# 604219</div>
  </div>

  <div class="brand">
    <div class="brand__name"><span class="brand__mark"></span>Keystead Mortgage</div>
    <div class="brand__slogan">your steady path home</div>
  </div>

  <div class="apply">
    <div class="apply__label">Apply online at :</div>
    <div class="apply__url">www.keystead.com</div>
  </div>

  <ul class="contact">
    <li class="contact__item">
      <svg class="contact__icon" viewBox="0 0 24 24" aria-hidden="true"><path d="M6.6 10.8a15 15 0 0 0 6.6 6.6l2.2-2.2c.3-.3.7-.4 1-.2 1.1.4 2.3.6 3.6.6.6 0 1 .4 1 1V20c0 .6-.4 1-1 1A17 17 0 0 1 3 4c0-.6.4-1 1-1h3.5c.6 0 1 .4 1 1 0 1.3.2 2.5.6 3.6.1.3 0 .7-.2 1Z" fill="var(--rust)"/></svg>
      (073) 555 - 0142
    </li>
    <li class="contact__item">
      <svg class="contact__icon" viewBox="0 0 24 24" aria-hidden="true"><rect x="6" y="2" width="12" height="20" rx="2" fill="none" stroke="var(--rust)" stroke-width="2"/><circle cx="12" cy="18" r="1.2" fill="var(--rust)"/></svg>
      (073) 555 - 0187
    </li>
    <li class="contact__item">
      <svg class="contact__icon" viewBox="0 0 24 24" aria-hidden="true"><rect x="2" y="5" width="20" height="14" rx="1" fill="var(--rust)"/><path d="M3 6l9 7 9-7" fill="none" stroke="var(--paper)" stroke-width="1.6"/></svg>
      dwhitfield@keystead.com
    </li>
    <li class="contact__address">4120 W Linden St Ste 300<br>Houston, TX 77041</li>
  </ul>

  <div class="lender-badge" role="img" aria-label="Fair Dwelling Creditor badge"></div>
</section>

</body>
</html>
```